Garden Design Business Card Design

A business card design for garden design company called ;
ROOTED IN CLAY which has a great deal of maintenance but
wishes to promote its expertise for design in planting and garden
design, but in an informal manner.

Would love to see quite a rustic approach,very strong and innovative and taking risks on typography. Am open to ideas with
colours,as memorability is important.

Target Market(s)

General public 40/50 years in a very trendy area

Industry/Entity Type

Business

Contact Information for Business Card

ROOTED IN CLAY. Garden design and maintenance.
Peter Holcombe
Telephone 01632 960417 Mobile 07700 900382

```html
<!DOCTYPE html>
<html lang="en">
<head>
<meta charset="UTF-8">
<title>Rooted in Clay – Business Card</title>
<link rel="stylesheet" href="https://fonts.googleapis.com/css2?family=Rubik+Dirt&family=Jura:wght@500&display=swap">
<style>
  :root {
    --page-bg: #e4e4e2;
    --wood-light: #9a4a1c;
    --wood-mid: #7a3814;
    --wood-dark: #2a1206;
    --leaf-green: #4fae3a;
    --grass-deep: #1f5a1c;
    --ink-black: #111111;
    --ink-grey: #a7a19c;
  }
  * { margin: 0; padding: 0; box-sizing: border-box; }
  html, body {
    width: 1200px;
    height: 900px;
    overflow: hidden;
    background: var(--page-bg);
  }
  .card {
    position: absolute;
    left: 100px;
    top: 130px;
    width: 1000px;
    height: 640px;
    overflow: hidden;
    background:
      radial-gradient(ellipse 75% 70% at 50% 45%, var(--wood-light) 0%, var(--wood-mid) 55%, var(--wood-dark) 100%);
    box-shadow: 0 14px 30px rgba(0,0,0,0.18);
  }
  .grass {
    position: absolute;
    left: 0;
    bottom: 0;
    width: 100%;
    height: 290px;
    background:
      linear-gradient(to bottom, rgba(108,194,74,0) 0%, rgba(108,194,74,0.55) 45%, var(--grass-deep) 100%);
  }
  .brand-name,
  .tagline,
  .person-name,
  .contact {
    position: absolute;
    white-space: nowrap;
  }
  .brand-name {
    left: 170px;
    top: 112px;
    font-family: "Rubik Dirt", "Impact", sans-serif;
    font-size: 68px;
    line-height: 1;
    font-weight: 400;
    color: var(--leaf-green);
  }
  .tagline {
    left: 174px;
    top: 186px;
    font-family: "Jura", "Arial", sans-serif;
    font-weight: 500;
    font-size: 37px;
    line-height: 1.1;
    color: var(--ink-black);
  }
  .person-name {
    left: 330px;
    top: 244px;
    font-family: "Rubik Dirt", "Impact", sans-serif;
    font-size: 58px;
    line-height: 1;
    font-weight: 400;
    text-transform: uppercase;
    color: var(--leaf-green);
  }
  .contact {
    left: 400px;
    top: 322px;
    font-family: "Jura", "Arial", sans-serif;
    font-weight: 500;
    font-size: 32px;
    line-height: 1.15;
    color: var(--ink-grey);
    border-collapse: collapse;
  }
  .contact td { padding: 0; }
  .contact .label { padding-right: 30px; }
</style>
</head>
<body>
  <main class="card">
    <div class="grass" role="img" aria-label="Tall blades of green grass rising along the bottom edge of the card"></div>
    <h1 class="brand-name">ROOTED IN CLAY</h1>
    <p class="tagline">Garden design and maintenance</p>
    <h2 class="person-name">Peter Holcombe</h2>
    <table class="contact">
      <tr><td class="label">Telephone</td><td>01632 960417</td></tr>
      <tr><td class="label">Mobile</td><td>07700 900382</td></tr>
    </table>
  </main>
</body>
</html>
```